needing web design for aerial and satellite installation comapny

We need our website designing, it needs to be professional and look creative,
We are a aerial and satellite company called Brindle Fixing & Tending ()
I like this site design also some of the following maybe:

https://www.corvimast.co.uk/

http://quellmoor.co.uk/

http://larkpin4guard.co.uk/portfolio/tdn-quellmoor/

The design will require coding once the design is complete, i haven't paid for this yet as i want to be sure the design is good before i commit.

The template needs to look professional and look like one of the leading companies.
The site will consist of all the features this site has https://www.corvimast.co.uk/

I like a modern design with the latest technology.

Target Market(s)

tv aerial satellite installation

Industry/Entity Type

Satellite Tv

Number of Pages Required

3 page

Font styles to use
Sans Serif

Colors

Designer to choose colors to be used in the design.

Requirements
Must have
• eb Contest Brief We need our website designing, it needs to be professional and look creative,
• We are a aerial and satellite company called Brindle Fixing Tending ()
• I like this site design also some of the following maybe:
• https://www.corvimast.co.uk/
• http://quellmoor.co.uk/
• http://larkpin4guard.co.uk/portfolio/tdn-quellmoor/
• The design will require coding once the design is complete, i haven't paid for this yet as i want to be sure the design is good before i commit.
• The template needs to look professional and look like one of the leading companies.
• The site will consist of all the features this site has https://www.corvimast.co.uk/
• I like a modern design with the latest technology.
Nice to have
• http://quellmoor.co.uk/
Should not have
• poor design

```html
<!DOCTYPE html>
<html lang="en">
<head>
<meta charset="utf-8">
<title>Brindle Fixing &amp; Tending — TV Aerial &amp; Satellite</title>
<link href="https://fonts.googleapis.com/css2?family=Roboto:wght@400;500;700;900&display=swap" rel="stylesheet">
<style>
:root{
  --yellow:#f6b400;
  --navy:#0f1a33;
  --ink:#222;
  --muted:#7b7b7b;
  --light:#f4f4f4;
  --line:#e6e6e6;
  --white:#fff;
  --social:#2f7fd0;
}
*{box-sizing:border-box;margin:0;padding:0}
html,body{width:1200px;height:4986px;overflow:hidden}
body{font-family:'Roboto',Arial,sans-serif;color:var(--ink);background:var(--white);position:relative}
.topbar,.site-header,.main-nav,.hero,.about,.services,.process,.why,.testimonials,.blog,.partners,.site-footer{position:absolute;left:0;width:1200px}
.section-title{position:absolute;left:106px;font-size:32px;font-weight:700;color:var(--ink)}
.section-title::after{content:"";position:absolute;left:0;top:50px;width:56px;height:4px;background:var(--yellow)}
.small{font-size:13px;line-height:19px;color:var(--muted)}

/* top bar */
.topbar{top:0;height:27px;background:var(--white);font-size:12px;color:#555}
.topbar .welcome{position:absolute;left:106px;top:6px}
.topbar .dark{position:absolute;right:0;top:0;width:660px;height:27px;background:var(--navy);clip-path:polygon(20px 0,100% 0,100% 100%,0 100%)}
.topbar .accent{position:absolute;right:652px;top:0;width:30px;height:27px;background:var(--yellow);clip-path:polygon(20px 0,30px 0,10px 100%,0 100%)}
.socials{position:absolute;left:955px;top:3px;display:flex;gap:8px}
.socials span{width:22px;height:21px;background:var(--social);display:block}

/* header */
.site-header{top:27px;height:99px;background:#f7f7f7}
.brand{position:absolute;left:106px;top:34px;display:flex;align-items:center;gap:10px}
.brand .mark{width:28px;height:28px;background:var(--yellow)}
.brand .name{font-size:20px;font-weight:700;color:var(--navy);letter-spacing:.3px;white-space:nowrap}
.contact-item{position:absolute;top:32px;display:flex;gap:10px;white-space:nowrap}
.contact-item svg{width:22px;height:22px;flex:none}
.contact-item b{display:block;font-size:13px;font-weight:700;color:var(--ink)}
.contact-item span{font-size:11px;color:#666}

/* nav */
.main-nav{top:126px;height:57px;border-top:1px solid var(--line);border-bottom:1px solid var(--line);background:var(--white)}
.main-nav a{position:absolute;top:19px;font-size:13px;font-weight:500;color:var(--ink);text-decoration:none;white-space:nowrap}

/* hero */
.hero{top:183px;height:615px;background:linear-gradient(100deg,#14161c 0%,#2a2e36 45%,#5d5a58 70%,#3a3c42 100%)}
.hero h1{position:absolute;left:140px;top:148px;font-size:54px;line-height:68px;font-weight:700;color:var(--white)}
.hero h1 em{font-style:normal;color:var(--yellow)}
.btn-pill{position:absolute;left:140px;top:466px;width:124px;height:36px;border-radius:18px;background:var(--yellow);color:var(--white);font-size:11px;font-weight:700;text-align:center;line-height:36px;letter-spacing:.5px}

/* about */
.about{top:798px;height:405px;background:var(--white)}
.feature{position:absolute;top:190px;width:300px;text-align:center}
.feature svg{width:36px;height:36px}
.feature h3{font-size:17px;font-weight:500;margin:12px 0 8px;color:#333}

/* services */
.services{top:1203px;height:785px;background:var(--light)}
.service{position:absolute;width:306px}
.service .photo{height:180px;position:relative}
.service .photo .tool{position:absolute;left:12px;bottom:12px;width:40px;height:40px;background:var(--yellow)}
.service h3{font-size:17px;font-weight:400;color:#333;margin-top:22px}
.service .bar{margin-top:10px;height:3px;width:306px;background:linear-gradient(90deg,var(--line) 0 40%,var(--yellow) 40% 100%)}

/* process */
.process{top:1988px;height:455px;background:var(--white)}
.step{position:absolute;top:179px;width:250px;text-align:center}
.step .circle{width:94px;height:94px;border-radius:50%;background:var(--yellow);margin:0 auto;display:flex;align-items:center;justify-content:center;box-shadow:0 0 0 8px #fdeec2}
.step h3{margin-top:26px;font-size:19px;font-weight:500;color:#333}
.step h3 b{color:var(--yellow);font-weight:700}
.step p{margin-top:8px}

/* why */
.why{top:2443px;height:449px;background:var(--light)}
.why .photo{position:absolute;left:0;top:0;width:592px;height:449px;background:linear-gradient(120deg,#1b2236,#3c3a47 55%,#7a4b4c)}
.stat{position:absolute;width:226px;height:127px;border:1px solid rgba(255,255,255,.8);color:var(--white);text-align:center;padding-top:28px}
.stat b{display:block;font-size:38px;font-weight:400}
.stat span{font-size:14px}
.why h2{position:absolute;left:618px;top:73px;font-size:30px;font-weight:700}
.why h2::after{content:"";position:absolute;left:0;top:44px;width:56px;height:4px;background:var(--yellow)}
.why .lead{position:absolute;left:618px;top:130px;width:480px}
.check{position:absolute;display:flex;align-items:center;gap:12px;font-size:11px;font-weight:700;color:#333}
.check i{width:20px;height:16px;background:var(--yellow);display:block;border-radius:2px}

/* testimonials */
.testimonials{top:2892px;height:498px;background:var(--white)}
.testimonial{position:absolute;top:176px;width:500px;height:223px}
.testimonial .face{position:absolute;left:0;top:0;width:210px;height:223px}
.testimonial .stripe{position:absolute;left:210px;top:0;width:10px;height:223px;background:var(--yellow)}
.testimonial p{position:absolute;left:250px;top:14px;width:236px;font-size:13px;line-height:19px;color:var(--muted)}
.testimonial p::before{content:"\201C";color:var(--navy);font-size:30px;font-weight:900;position:absolute;left:-24px;top:-4px}

/* blog */
.blog{top:3390px;height:692px;background:var(--light)}
.post{position:absolute;top:167px;width:306px;height:465px;background:var(--white)}
.post .photo{height:216px}
.post .body{padding:26px 16px 0}
.post .date{font-size:12px;color:#888}
.post h3{font-size:17px;font-weight:700;margin:12px 0 10px}
.post .more{display:block;margin-top:24px;font-size:13px;font-weight:700;color:var(--yellow)}

/* partners */
.partners{top:4082px;height:366px;background:var(--white)}
.partner{position:absolute;top:110px;width:170px;height:150px;display:flex;align-items:center;justify-content:center;gap:8px;font-size:20px;font-weight:700;color:#555}
.partner i{width:16px;height:16px;border-radius:50%;background:#9aa3b5;display:block}
.dots{position:absolute;left:490px;top:322px;display:flex;gap:12px}
.dots span{width:7px;height:7px;border-radius:50%;background:#cfcfcf}
.dots span:first-child{background:#666}

/* footer */
.site-footer{top:4514px;height:472px;background:linear-gradient(180deg,var(--navy) 0%,#0b1428 100%)}
.subscribe{position:absolute;left:100px;top:4430px;width:997px;height:156px;background:var(--yellow);z-index:2}
.subscribe .label{position:absolute;left:80px;top:60px;font-size:26px;font-weight:700;color:var(--navy)}
.subscribe .icon{position:absolute;left:26px;top:56px;width:36px;height:36px;border:2px solid var(--navy);transform:rotate(-12deg)}
.subscribe .field{position:absolute;left:422px;top:56px;width:334px;height:44px;background:var(--white);font-size:12px;color:#aaa;padding:14px 14px}
.subscribe .submit{position:absolute;left:756px;top:56px;width:143px;height:44px;background:var(--navy);color:var(--white);font-size:12px;font-weight:700;text-align:center;line-height:44px}
.fcol{position:absolute;top:130px;color:var(--white)}
.fcol h4{font-size:16px;font-weight:700;margin-bottom:26px}
.fcol p{font-size:12px;line-height:17px;color:#c9ccd4;width:260px}
.footer-brand{display:flex;align-items:center;gap:10px;margin-bottom:18px}
.footer-brand .mark{width:28px;height:28px;background:var(--yellow)}
.footer-brand .name{font-size:17px;font-weight:700;color:var(--white);white-space:nowrap}
.links{display:grid;grid-template-columns:150px 150px;row-gap:9px;font-size:12px;color:#d8dbe2}
.links span::before{content:"\25B8";color:var(--yellow);margin-right:8px}
.info{font-size:12px;line-height:20px;color:#d8dbe2;white-space:nowrap}
.info b{display:inline-block;width:62px;color:var(--white)}
.fsocial{display:flex;gap:20px;margin-top:24px}
.fsocial span{width:10px;height:10px;background:#c9ccd4;display:block;border-radius:2px}
.bottom-bar{position:absolute;left:0;top:422px;width:1200px;height:50px;border-top:1px solid rgba(255,255,255,.1)}
.bottom-links{position:absolute;right:100px;top:18px;display:flex;gap:22px;font-size:10px;color:#c9ccd4}
</style>
</head>
<body>

<div class="topbar">
  <span class="welcome">Welcome To Our Official Site</span>
  <div class="accent"></div>
  <div class="dark"></div>
  <div class="socials"><span></span><span></span><span></span><span></span></div>
</div>

<header class="site-header">
  <div class="brand"><span class="mark"></span><span class="name">BRINDLE FIXING &amp; TENDING</span></div>
  <div class="contact-item" style="left:655px">
    <svg viewBox="0 0 24 24"><path d="M12 2a7 7 0 0 0-7 7c0 5 7 13 7 13s7-8 7-13a7 7 0 0 0-7-7zm0 9.5A2.5 2.5 0 1 1 12 6.5a2.5 2.5 0 0 1 0 5z" fill="#f6b400"/></svg>
    <div><b>Our Location</b><span>Harlow Vale, TX 70250</span></div>
  </div>
  <div class="contact-item" style="left:820px">
    <svg viewBox="0 0 24 24"><rect x="2" y="5" width="20" height="14" rx="2" fill="#f6b400"/><path d="M3 6l9 7 9-7" stroke="#fff" stroke-width="1.5" fill="none"/></svg>
    <div><b>Send Us Mail</b><span>mail@brindle.example</span></div>
  </div>
  <div class="contact-item" style="left:982px">
    <svg viewBox="0 0 24 24"><path d="M6.6 10.8a15 15 0 0 0 6.6 6.6l2.2-2.2a1 1 0 0 1 1-.25 11.4 11.4 0 0 0 3.6.57 1 1 0 0 1 1 1V20a1 1 0 0 1-1 1A17 17 0 0 1 3 4a1 1 0 0 1 1-1h3.5a1 1 0 0 1 1 1c0 1.25.2 2.45.57 3.57a1 1 0 0 1-.25 1z" fill="#f6b400"/></svg>
    <div><b>Call Us</b><span>+100 222 3344</span></div>
  </div>
</header>

<nav class="main-nav">
  <a style="left:133px">Home</a>
  <a style="left:226px">TV Area Services</a>
  <a style="left:389px">Services</a>
  <a style="left:485px">Halcyon Satellite TV</a>
  <a style="left:651px">Smart Home</a>
  <a style="left:775px">Communal TV</a>
  <a style="left:917px">Contact Us</a>
</nav>

<section class="hero" role="img" aria-label="Technician fitting a satellite dish on a wall">
  <h1>We' Re Into Smart<br>Home TV Aerial &amp;<br>Satellite <em>Installers</em><br><em>&amp; Repairs</em></h1>
  <span class="btn-pill">CONTACT US</span>
</section>

<section class="about">
  <h2 class="section-title" style="top:80px">About Us</h2>
  <div class="feature" style="left:109px">
    <svg viewBox="0 0 24 24"><circle cx="12" cy="7" r="4" fill="#f6b400"/><circle cx="5" cy="9" r="3" fill="#f6b400"/><circle cx="19" cy="9" r="3" fill="#f6b400"/><path d="M4 20c0-4 4-7 8-7s8 3 8 7z" fill="#f6b400"/></svg>
    <h3>Qualified Agents</h3>
    <p class="small">Lorem ipsum dolor sit amet, consectetur<br>adipiscing elit. Cras mollis, leo a<br>condimentum vehicula</p>
  </div>
  <div class="feature" style="left:442px">
    <svg viewBox="0 0 24 24"><rect x="2" y="6" width="20" height="12" rx="1" fill="none" stroke="#f6b400" stroke-width="2"/><circle cx="12" cy="12" r="3" fill="#f6b400"/></svg>
    <h3>Fair Prices</h3>
    <p class="small">Lorem ipsum dolor sit amet, consectetur<br>adipiscing elit. Cras mollis, leo a<br>condimentum vehicula</p>
  </div>
  <div class="feature" style="left:774px">
    <svg viewBox="0 0 24 24"><path d="M12 2l3 7h7l-5.5 4.5 2 7.5L12 16.5 5.5 21l2-7.5L2 9h7z" fill="#f6b400"/></svg>
    <h3>Best Offers</h3>
    <p class="small">Lorem ipsum dolor sit amet, consectetur<br>adipiscing elit. Cras mollis, leo a<br>condimentum vehicula</p>
  </div>
</section>

<section class="services">
  <h2 class="section-title" style="top:80px">Provide Services</h2>
  <div class="service" style="left:106px;top:180px"><div class="photo" role="img" aria-label="Aerial mast on a chimney against blue sky" style="background:linear-gradient(160deg,#4f8fe0,#2b6cc4 60%,#8a5a3a)"><span class="tool"></span></div><h3>TV Aerial Services</h3><div class="bar"></div></div>
  <div class="service" style="left:439px;top:180px"><div class="photo" role="img" aria-label="Installer adjusting a satellite dish" style="background:linear-gradient(150deg,#2c2c2c,#6f6f6f 55%,#bdbdbd)"><span class="tool"></span></div><h3>Halcyon Satelite TV</h3><div class="bar"></div></div>
  <div class="service" style="left:771px;top:180px"><div class="photo" role="img" aria-label="Living room with mounted television" style="background:linear-gradient(150deg,#d8d2c8,#a49a8c 60%,#5a4e44)"><span class="tool"></span></div><h3>Sound &amp; Vision</h3><div class="bar"></div></div>
  <div class="service" style="left:106px;top:469px"><div class="photo" role="img" aria-label="Smart home house model with phone control" style="background:linear-gradient(150deg,#f2f2f2,#d9c9b5 55%,#b64a3c)"><span class="tool"></span></div><h3>Smart Home System</h3><div class="bar"></div></div>
  <div class="service" style="left:439px;top:469px"><div class="photo" role="img" aria-label="Glowing wifi signal on dark background" style="background:radial-gradient(circle at 55% 50%,#e8b25c,#6a3f1d 45%,#1a130e)"><span class="tool"></span></div><h3>Wifi Solution</h3><div class="bar"></div></div>
  <div class="service" style="left:771px;top:469px"><div class="photo" role="img" aria-label="Apartment building with communal dishes" style="background:linear-gradient(150deg,#9a9fa6,#6b6f76 55%,#3d4047)"><span class="tool"></span></div><h3>Communal TV System</h3><div class="bar"></div></div>
</section>

<section class="process">
  <h2 class="section-title" style="top:86px">Work Process</h2>
  <div class="step" style="left:91px">
    <div class="circle"><svg width="36" height="36" viewBox="0 0 24 24"><circle cx="12" cy="12" r="9" fill="none" stroke="#fff" stroke-width="2"/><path d="M12 12V3a9 9 0 0 1 9 9z" fill="#fff"/></svg></div>
    <h3><b>01.</b> Contact Us</h3>
    <p class="small">Lorem ipsum dolor sit amet,<br>consectetur adipiscing elit.</p>
  </div>
  <div class="step" style="left:340px">
    <div class="circle"><svg width="36" height="36" viewBox="0 0 24 24"><rect x="2" y="6" width="20" height="12" fill="none" stroke="#fff" stroke-width="2"/><circle cx="12" cy="12" r="2.5" fill="#fff"/></svg></div>
    <h3><b>02.</b> Make Payment</h3>
    <p class="small">Lorem ipsum dolor sit amet,<br>consectetur adipiscing elit.</p>
  </div>
  <div class="step" style="left:590px">
    <div class="circle"><svg width="36" height="36" viewBox="0 0 24 24"><circle cx="6" cy="16" r="4" fill="none" stroke="#fff" stroke-width="2"/><circle cx="18" cy="16" r="4" fill="none" stroke="#fff" stroke-width="2"/><path d="M6 16l4-8h5l3 8M10 8l2 8" fill="none" stroke="#fff" stroke-width="2"/></svg></div>
    <h3><b>03.</b> Staff Sent</h3>
    <p class="small">Lorem ipsum dolor sit amet,<br>consectetur adipiscing elit.</p>
  </div>
  <div class="step" style="left:839px">
    <div class="circle"><svg width="36" height="36" viewBox="0 0 24 24"><path d="M4 12l5 5L20 6" fill="none" stroke="#fff" stroke-width="3"/></svg></div>
    <h3><b>04.</b> Fix It</h3>
    <p class="small">Lorem ipsum dolor sit amet,<br>consectetur adipiscing elit.</p>
  </div>
</section>

<section class="why">
  <div class="photo" role="img" aria-label="Technician on a rooftop at dusk"></div>
  <div class="stat" style="left:93px;top:83px"><b>17</b><span>Projects Finished</span></div>
  <div class="stat" style="left:336px;top:83px"><b>10</b><span>Happy Clients</span></div>
  <div class="stat" style="left:93px;top:233px"><b>8</b><span>Our Team</span></div>
  <div class="stat" style="left:336px;top:233px"><b>13</b><span>Hours of Work</span></div>
  <h2>Why Choose Us</h2>
  <p class="lead small">Lorem Ipsum is simply dummy text of the printing and typesetting industry. Lorem Ipsum has been the industry's standard dummy text ever since the 1500s, when an unknown printer took a galley of type and scrambled it to make a type specimen book.</p>
  <div class="check" style="left:618px;top:263px"><i></i>EXPERT &amp; PROFESSIONAL</div>
  <div class="check" style="left:848px;top:263px"><i></i>PROFESSIONAL APPROACH</div>
  <div class="check" style="left:618px;top:306px"><i></i>HIGHT QUALITY WORK</div>
  <div class="check" style="left:848px;top:306px"><i></i>SATISFACTION GUARANTEE</div>
  <div class="check" style="left:618px;top:346px"><i></i>QUICK IN RESPONSE</div>
  <div class="check" style="left:848px;top:346px"><i></i>24/7 EMERGENCY</div>
</section>

<section class="testimonials">
  <h2 class="section-title" style="top:86px">Our testimonial</h2>
  <div class="testimonial" style="left:106px">
    <div class="face" role="img" aria-label="Portrait of a client" style="background:linear-gradient(160deg,#d9d9d9,#a8a8a8)"></div>
    <div class="stripe"></div>
    <p>Lorem Ipsum is simply dummy text of the printing and typesetting industry. Lorem Ipsum has been the industry's standard dummy text ever since the 1500s, when an unknown printer took a galley of type and scrambled it to make a type. &#8221;</p>
  </div>
  <div class="testimonial" style="left:605px">
    <div class="face" role="img" aria-label="Portrait of a client" style="background:linear-gradient(160deg,#c9b8a6,#6e5a48)"></div>
    <div class="stripe"></div>
    <p>Lorem Ipsum is simply dummy text of the printing and typesetting industry. Lorem Ipsum has been the industry's standard dummy text ever since the 1500s, when an unknown printer took a galley of type and scrambled it to make a type. &#8221;</p>
  </div>
</section>

<section class="blog">
  <h2 class="section-title" style="top:70px">Our Blog</h2>
  <article class="post" style="left:106px">
    <div class="photo" role="img" aria-label="Satellite dish on a wall" style="background:linear-gradient(160deg,#c4c7cc,#7e848c)"></div>
    <div class="body"><div class="date">June 24th 2015</div><h3>Hollinreach Plans</h3><p class="small">Lorem Ipsum is simply dummy text of the printing and typesetting industry. Lorem Ipsum has been the industry's standard dummy text ever since the 1500s.</p><span class="more">More ›</span></div>
  </article>
  <article class="post" style="left:439px">
    <div class="photo" role="img" aria-label="Hands repairing a circuit board" style="background:linear-gradient(160deg,#3a2e26,#8a6a4a 55%,#2a2520)"></div>
    <div class="body"><div class="date">June 24th 2015</div><h3>Paid Referral Program</h3><p class="small">Lorem Ipsum is simply dummy text of the printing and typesetting industry. Lorem Ipsum has been the industry's standard dummy text ever since the 1500s.</p><span class="more">More ›</span></div>
  </article>
  <article class="post" style="left:771px">
    <div class="photo" role="img" aria-label="Large satellite dish against the sky" style="background:linear-gradient(160deg,#e6e8ea,#9aa0a6)"></div>
    <div class="body"><div class="date">June 24th 2015</div><h3>Tessery Orders</h3><p class="small">Lorem Ipsum is simply dummy text of the printing and typesetting industry. Lorem Ipsum has been the industry's standard dummy text ever since the 1500s.</p><span class="more">More ›</span></div>
  </article>
</section>

<section class="partners">
  <div class="partner" style="left:100px"><i></i>Quillsat</div>
  <div class="partner" style="left:295px"><i></i>Marrowcast</div>
  <div class="partner" style="left:500px;font-size:24px"><i></i>Veltrace</div>
  <div class="partner" style="left:705px"><i></i>Quillsat</div>
  <div class="partner" style="left:905px"><i></i>Marrowcast</div>
  <div class="dots"><span></span><span></span><span></span><span></span><span></span><span></span><span></span><span></span><span></span><span></span></div>
</section>

<div class="subscribe">
  <span class="icon"></span>
  <span class="label">SUBSCRIBE OUR NEWS</span>
  <span class="field">Enter Your Email</span>
  <span class="submit">SUBMIT</span>
</div>

<footer class="site-footer">
  <div class="fcol" style="left:113px">
    <h4>ABOUT US</h4>
    <div class="footer-brand"><span class="mark"></span><span class="name">BRINDLE FIXING &amp; TENDING</span></div>
    <p>Aenean suscipit eget mi act fermentum phasellus vulputate turpis tincidunt. Aenean suscipit eget mi act fermentum phasellus vulputate turpis tincidunt. Aenean suscipit eget mi act fermentum phasellus.</p>
  </div>
  <div class="fcol" style="left:445px">
    <h4>COMPANY LINKS</h4>
    <div class="links">
      <span>History</span><span>Services</span>
      <span>Team &amp; Awards</span><span>Delivery Methods</span>
      <span>Community</span><span>Safety</span>
      <span>News &amp; Events</span><span>Sustainability</span>
      <span>FAQ</span><span>Portfolio</span>
      <span>Contact Us</span><span>Shop</span>
    </div>
  </div>
  <div class="fcol" style="left:778px">
    <h4>CONTACT INFO</h4>
    <div class="info">
      <div><b>Address:</b>48 Quarry Lane, Unit 3,</div>
      <div><b></b>Ashcombe, AB1 2CD</div>
      <div style="margin-top:8px"><b>Phone:</b>+44 (0) 200 555 0147</div>
      <div><b>E-mail:</b>office@brindle.example</div>
    </div>
    <div class="fsocial"><span></span><span></span><span></span><span></span><span></span><span></span></div>
  </div>
  <div class="bottom-bar"><div class="bottom-links"><span>HISTORY</span><span>FAQ</span><span>EVENTS</span></div></div>
</footer>

</body>
</html>
```